Need Brochure Design For Pizza Restaurant

Need redesign for pizza restaurant. Brochure size is 11 Inches X 17 Inches Roll Fold.

Specifications and original menu will be attached.

Target Market(s)

Those who enjoy Pizza ;)

Industry/Entity Type

Restaurant

Requirements
Must have
• The brochure must be double sided.

Must include important information such as operating hours, telephone number, etc.

The brochure should have a snapshot of a map such as Trellan Charts showing the location of the establishment.

All these information could be found on our Trellan Spots page:
http://charts.trellan.example/charts?hl=en&sugexp=frgbld&gs_nf=1&pq=ro+pizza&cp=9&gs_id=4&xhr=t&q=ro%20pizza%20fort%20mcmurray&bav=on.2,or.r_gc.r_pw.r_qf.,cf.osb&biw=1584&bih=810&um=1&ie=UTF-8&sa=N&tab=il

There should be a place where the receiver can cut out a piece of the menu to get a coupon, like in the original design I attached, in which case, there should not be anything important on the reverse side of the brochure where the cut out is to be made.

Final copy needs to be in PDF and PSD, the latter must be separated into layers for ease of later editing.
Nice to have
• Highlight the importance that the establishment is under new management and recently renovated.

```html
<!DOCTYPE html>
<html lang="en">
<head>
<meta charset="utf-8">
<title>Hollinger Pizza Tavern Menu</title>
<link href="https://fonts.googleapis.com/css2?family=Alfa+Slab+One&family=Archivo+Narrow:wght@400;700&family=Arimo:wght@400;700&display=swap" rel="stylesheet">
<style>
:root{
  --paper:#ffffff;
  --ink:#111111;
  --red:#e0261b;
  --band:#111111;
  --muted:#333333;
  --rule:#cccccc;
}
*{box-sizing:border-box;margin:0;padding:0}
html,body{width:1200px;height:776px;overflow:hidden;background:var(--paper)}
.menu{position:relative;width:1200px;height:776px;background:var(--paper);font-family:"Arimo",Arial,sans-serif;color:var(--ink)}
.abs{position:absolute}
.section-title{position:absolute;font-family:"Alfa Slab One",Georgia,serif;font-size:17px;letter-spacing:1px;color:var(--ink);white-space:nowrap}
.section-title .hi{color:var(--red)}
.item{display:flex;justify-content:space-between;gap:4px;font-family:"Archivo Narrow",Arial,sans-serif;font-weight:700;font-size:12.5px;line-height:13px;white-space:nowrap}
.desc{font-size:7px;line-height:8px;color:var(--muted);padding-left:6px;position:relative}
.desc::before{content:"";position:absolute;left:0;top:2px;width:4px;height:4px;border-radius:50%;background:var(--ink)}
.photo{position:absolute}

.salads{left:128px;top:44px;width:252px}
.salads .entry{height:31px}
.steaks{left:22px;top:309px;width:358px}
.steaks .entry{height:24px}
.burgers{left:22px;top:467px;width:360px}
.burgers .entry{height:24px}

.happy{left:455px;top:42px;font-size:10.5px;color:var(--ink)}
.happy b{color:var(--red)}
.drinks{top:64px;font-family:"Archivo Narrow",Arial,sans-serif}
.drinks .day{font-weight:700;font-size:12.5px;line-height:13px}
.drinks .row{display:flex;justify-content:space-between;font-size:10.5px;line-height:11.5px;color:var(--muted)}
.drinks .row span:last-child{color:var(--ink)}

.fav{left:430px;top:244px;width:362px}
.fav .entry{height:28px}
.fav .desc{margin-top:3px}

.desserts{left:430px;top:672px;width:168px}
.desserts .item{font-size:12px;line-height:13.8px}

.brand{left:835px;top:24px;width:365px;text-align:center;font-family:"Arimo",Arial,sans-serif;font-weight:700;font-size:26px;line-height:30px;color:var(--ink);white-space:nowrap}
.phone{left:835px;top:66px;width:365px;text-align:center;font-family:"Arimo",Arial,sans-serif;font-weight:700;font-size:17px;letter-spacing:1px}

.sand{left:838px;top:134px;width:172px}
.pasta{left:1028px;top:134px;width:170px}
.sand .entry,.pasta .entry{margin-bottom:5px}
.sand .item,.pasta .item{font-size:11px;line-height:12px}
.sand .desc,.pasta .desc{font-size:6.5px;line-height:7.5px}
.divider{left:1018px;top:110px;width:1px;height:360px;background:var(--rule)}

.web{left:838px;top:482px;width:362px;height:28px;background:var(--band);color:#fff;font-weight:700;font-size:13px;display:flex;align-items:center;justify-content:center}
.info{left:1030px;top:522px;width:165px;color:#fff;font-weight:700;font-size:11px;line-height:14px;text-align:center}
.info p{margin-bottom:8px}
.ownership-banner{left:850px;top:755px;font-family:"Alfa Slab One",Georgia,serif;color:#fff;font-size:11px;letter-spacing:2px}
.new-tag{left:628px;top:660px;font-family:"Alfa Slab One",Georgia,serif;font-size:13px;color:var(--ink);transform:rotate(-14deg);white-space:nowrap}
.new-tag .hi{color:var(--red)}
</style>
</head>
<body>
<main class="menu">

  <div class="photo" role="img" aria-label="Photo of a fresh garden salad with tomatoes beside an olive oil bottle" style="left:0;top:0;width:125px;height:262px;background:radial-gradient(ellipse at 40% 75%,#6fa82e 0%,#3d7a1c 35%,#c9d98a 55%,#ffffff 72%),linear-gradient(#d9b24a,#fff);border-radius:0 0 60px 0"></div>
  <div class="photo" role="img" aria-label="Photo of a large cheeseburger with lettuce, tomato and onion" style="left:40px;top:612px;width:300px;height:164px;background:radial-gradient(ellipse at 50% 55%,#c9893a 0%,#8a4a1e 30%,#e9b53a 45%,#3f8a2a 55%,#c23a20 62%,#e9a84a 75%,#ffffff 100%);border-radius:50% 50% 10px 10px"></div>

  <h2 class="section-title" style="left:160px;top:20px"><span class="hi">H</span>ouse <span class="hi">S</span>alads</h2>
  <div class="abs salads">
    <div class="entry"><div class="item"><span>House Salad</span><span>$8.95</span></div><p class="desc">House salad with head lettuce, carrots, purple cabbage, celery, cucumber &amp; tomatoes.</p></div>
    <div class="entry"><div class="item"><span>Greek Salad</span><span>$9.95</span></div><p class="desc">Lettuce, green peppers, tomatoes, cucumber, olives &amp; feta cheese served with our secret house dressing.</p></div>
    <div class="entry"><div class="item"><span>Caesar Salad</span><span>$8.95</span></div><p class="desc">Crisp romaine lettuce tossed in our Caesar dressing &amp; topped with Parmesan cheese, bacon bits &amp; croutons.</p></div>
    <div class="entry"><div class="item"><span>Avocado Chicken Salad</span><span>$13.95</span></div><p class="desc">Fresh garden salad, sliced ripe avocados, bacon bits, cheese &amp; grilled chicken served with balsamic dressing.</p></div>
    <div class="entry"><div class="item"><span>Chef's Salad</span><span>$11.95</span></div><p class="desc">Just like our house salad, but we topped it with turkey, ham, bacon bits, cheese &amp; boiled eggs.</p></div>
    <div class="entry"><div class="item"><span>Blackened Chicken</span><span>$11.95</span></div><p class="desc">Grilled blackened chicken seasoned with our blackened spice. Served over fresh garden greens with cheese &amp; bacon bits.</p></div>
    <div class="entry"><div class="item"><span>Blackened Salmon</span><span>$13.95</span></div><p class="desc">Grilled blackened salmon seasoned with our blackened spice. Served over fresh garden greens with cheese &amp; bacon bits.</p></div>
  </div>

  <h2 class="section-title" style="left:155px;top:285px"><span class="hi">S</span>te<span class="hi">aks</span></h2>
  <div class="abs steaks">
    <div class="entry"><div class="item"><span>Sirloin Steak Sandwich</span><span>$14.95</span></div><p class="desc">6 oz. of charbroiled Alberta beef to your liking. Served on garlic toast.</p></div>
    <div class="entry"><div class="item"><span>Prime Rib Steak</span><span>$22.95</span></div><p class="desc">12 oz. flame grilled steak cooked to perfection and brushed with garlic butter.</p></div>
    <div class="entry"><div class="item"><span>T-Bone Steak</span><span>$21.95</span></div><p class="desc">14oz. king of steaks. This massive beast is 100% Alberta beef and is flame grilled to perfection.</p></div>
    <div class="entry"><div class="item"><span>Rib-Eye Steak</span><span>$20.95</span></div><p class="desc">10 oz. of delicious rib eye charbroiled to perfection with steak spices and brushed with garlic butter.</p></div>
    <div class="entry"><div class="item"><span>New York Steak</span><span>$19.95</span></div><p class="desc">8 oz. flame grilled steak cooked to perfection and brushed with garlic butter.</p></div>
  </div>

  <h2 class="section-title" style="left:98px;top:447px"><span class="hi">H</span>ouse <span class="hi">B</span>urgers</h2>
  <div class="abs burgers">
    <div class="entry"><div class="item"><span>House Burger</span><span>$10.95</span></div><p class="desc">6 oz. Alberta beef topped with cheddar cheese, lettuce, tomato and bacon.</p></div>
    <div class="entry"><div class="item"><span>Blackened Chicken Burger</span><span>$10.95</span></div><p class="desc">6 oz. charbroiled chicken breast topped with bacon and cheese. Hot and spicy.</p></div>
    <div class="entry"><div class="item"><span>Prime Rib Burger</span><span>$11.95</span></div><p class="desc">Mouthwatering prime rib patty served cheddar cheese, lettuce, tomato and bacon.</p></div>
    <div class="entry"><div class="item"><span>Chicken Club Burger</span><span>$10.95</span></div><p class="desc">Grilled chicken breasts topped with cheddar cheese, bacon, lettuce, tomato and mayonnaise.</p></div>
    <div class="entry"><div class="item"><span>Lotza Mushroom Burger</span><span>$10.95</span></div><p class="desc">6 oz. Alberta beef patty topped with mozzarella cheese, bacon and loads of mushrooms.</p></div>
    <div class="entry"><div class="item"><span>Crispy Chicken Burger</span><span>$11.95</span></div><p class="desc">Breaded chicken breast deep-fried golden with cheddar cheese, lettuce, tomato and mayonnaise.</p></div>
  </div>

  <h2 class="section-title" style="left:508px;top:18px">D<span class="hi">rink</span> S<span class="hi">pec</span>ials</h2>
  <p class="abs happy"><b>Happy Hour Every Day</b> - Sunday through Saturday 11:00 am-7:00 pm</p>
  <div class="abs drinks" style="left:432px;width:176px">
    <div class="day">Monday</div>
    <div class="row"><span>Coral Rum AND Maplecrest</span><span>$4.50</span></div>
    <div class="day">Tuesday</div>
    <div class="row"><span>Import Beer</span><span>$5.00</span></div>
    <div class="row"><span>Tequila</span><span>$4.50</span></div>
    <div class="day">Wednesday</div>
    <div class="row"><span>Jug of Draft</span><span>$15.00</span></div>
    <div class="row"><span>Frost Beer</span><span>$4.50</span></div>
    <div class="row"><span>Wings Each</span><span>$.35</span></div>
    <div class="day">Thursday</div>
    <div class="row"><span>Bucket of Beer</span><span>$22.50</span></div>
    <div class="row"><span>Bert Raymond's</span><span>$4.50</span></div>
  </div>
  <div class="abs drinks" style="left:623px;width:182px">
    <div class="day">Friday</div>
    <div class="row"><span>Golden Draft</span><span>$5.00</span></div>
    <div class="row"><span>High Ball</span><span>$4.50</span></div>
    <div class="day">Saturday</div>
    <div class="row"><span>Pint Draft</span><span>$4.50</span></div>
    <div class="row"><span>Pony Jug</span><span>$15.00</span></div>
    <div class="day">Sunday</div>
    <div class="row"><span>Caesar's</span><span>$4.50</span></div>
    <div class="row"><span>Sambuca</span><span>$4.50</span></div>
    <div class="row"><span>Wings Each</span><span>$.35</span></div>
  </div>

  <h2 class="section-title" style="left:545px;top:218px">F<span class="hi">avo</span>rit<span class="hi">es</span></h2>
  <div class="abs fav">
    <div class="entry"><div class="item"><span>Hot Beef Sandwich</span><span>$13.95</span></div><p class="desc">Shaved meat piled high on bread and smothered in gravy.</p></div>
    <div class="entry"><div class="item"><span>Hot Turkey Sandwich</span><span>$13.95</span></div><p class="desc">Shaved meat piled high on bread and smothered in gravy.</p></div>
    <div class="entry"><div class="item"><span>Hot Hamburger Sandwich</span><span>$13.95</span></div><p class="desc">This is an all time favorite at Hollinger's. Home made beef patty on bread and smothered with gravy.</p></div>
    <div class="entry"><div class="item"><span>Blackened Salmon</span><span>$15.95</span></div><p class="desc">Grilled blackened chicken seasoned with our blackened spice.</p></div>
    <div class="entry"><div class="item"><span>Pork Chop</span><span>$13.95</span></div><p class="desc">Grilled pork chips topped with sautéed onions and served with applesauce.</p></div>
    <div class="entry"><div class="item"><span>Liver and Onion</span><span>$13.95</span></div><p class="desc">Tender beef liver grilled to perfection topped with sautéed onions and smothered in gravy.</p></div>
    <div class="entry"><div class="item"><span>Chicken Parmesan</span><span>$14.95</span></div><p class="desc">A breaded chicken breast covered in meat sauce and melted mozzarella cheese.</p></div>
    <div class="entry"><div class="item"><span>Veal Parmesan</span><span>$14.95</span></div><p class="desc">A breaded veal cutlet covered in meat sauce and melted mozzarella cheese.</p></div>
    <div class="entry"><div class="item"><span>Fish and Chips</span><span>$12.95</span></div><p class="desc">Two pieces of cod dipped in our homemade beer batter. Served with tartar sauce.</p></div>
    <div class="entry"><div class="item"><span>Half BBQ Chicken</span><span>$13.95</span></div><p class="desc">Our oven roasted chicken is a must try.</p></div>
    <div class="entry"><div class="item"><span>Chicken Fingers</span><span>$12.50</span></div><p class="desc">Breaded chicken fingers deep-fried golden served with plum sauce.</p></div>
    <div class="entry"><div class="item"><span>Rack of Back Ribs</span><span>$19.95</span></div><p class="desc">Tender back of baby back ribs covered in a tangy BBQ sauce.</p></div>
    <div class="entry"><div class="item"><span>Chicken Bowl</span><span>$12.95</span></div><p class="desc">Fresh garden vegetable stir-fried with chicken in honey garlic sauce. Served on rice or noodles.</p></div>
    <div class="entry"><div class="item"><span>Seafood Bowl</span><span>$12.95</span></div><p class="desc">Fresh garden vegetable stir-fried with shrimp and scallop in honey garlic sauce. Served on rice or noodles</p></div>
  </div>

  <h2 class="section-title" style="left:482px;top:644px">D<span class="hi">e</span>sse<span class="hi">rts</span></h2>
  <div class="abs desserts">
    <div class="item"><span>Lemon Meringue Pie</span><span>$5.95</span></div>
    <div class="item"><span>Apple Pie</span><span>$5.95</span></div>
    <div class="item"><span>Coconut Cream Pie</span><span>$5.95</span></div>
    <div class="item"><span>Cheesecake</span><span>$6.95</span></div>
    <div class="item"><span>Blueberry Pie</span><span>$5.95</span></div>
    <div class="item"><span>355mL Canned Pop</span><span>$1.99</span></div>
    <div class="item"><span>2.0L Bottled Pop</span><span>$3.49</span></div>
  </div>
  <p class="abs new-tag"><span class="hi">New</span> Ownership!</p>
  <div class="photo" role="img" aria-label="Photo of a slice of pie with apple slices and mint" style="left:622px;top:680px;width:178px;height:92px;border-radius:50%;background:radial-gradient(ellipse at 50% 50%,#e9c46a 0%,#c98a3a 40%,#a7c46a 65%,#f2efe6 85%)"></div>

  <h1 class="abs brand">Hollinger Pizza Tavern</h1>
  <p class="abs phone">780-555-0142</p>

  <h2 class="section-title" style="left:842px;top:106px"><span class="hi">S</span>and<span class="hi">wich</span>es</h2>
  <h2 class="section-title" style="left:1075px;top:106px">P<span class="hi">asta</span></h2>
  <div class="abs divider"></div>

  <div class="abs sand">
    <div class="entry"><div class="item"><span>Monte Cristo</span><span>$10.95</span></div><p class="desc">Ham, turkey and mozzarella cheese served triple decker style on egg dipped grilled bread.</p></div>
    <div class="entry"><div class="item"><span>Tavern Brute</span><span>$10.95</span></div><p class="desc">This deli styled sandwich is loaded with salami, pepperoni, smoked ham, mozzarella cheese, onions and pizza sauce served on a sub bun.</p></div>
    <div class="entry"><div class="item"><span>Club House</span><span>$10.95</span></div><p class="desc">Triple-decker classic with turkey, bacon, tomato, lettuce, cheddar cheese and mayonnaise.</p></div>
    <div class="entry"><div class="item"><span>Raging Beef Sandwich</span><span>$10.95</span></div><p class="desc">A classic beef dip sandwich spiffed up with mushrooms and mozzarella cheese.</p></div>
    <div class="entry"><div class="item"><span>Avocado Chicken Sandwich</span><span>$12.95</span></div><p class="desc">Avocado, grilled chicken, tomato, lettuce and mayonnaise on a toasted bun.</p></div>
    <div class="entry"><div class="item"><span>Ultimate Club</span><span>$12.95</span></div><p class="desc">This triple decker sandwich is loaded with turkey, bacon, ham, roast beef, lettuce, tomato, cheese and jalapeno mayonnaise.</p></div>
    <div class="entry"><div class="item"><span>Steak on the Bun</span><span>$14.95</span></div><p class="desc">As delicious as you'd think.</p></div>
    <div class="entry"><div class="item"><span>BLT</span><span>$8.95</span></div><p class="desc">Classic sandwich with bacon, lettuce, tomato and mayonnaise on a toasted bun.</p></div>
    <div class="entry"><div class="item"><span>Denver Sandwich</span><span>$8.95</span></div><p class="desc">Onions and ham grilled with eggs and cheddar on western toast.</p></div>
  </div>

  <div class="abs pasta">
    <div class="entry"><div class="item"><span>Chicken Mushroom Fettuccini</span><span>$14.95</span></div><p class="desc">Pasta covered in creamy white wine sauce with bacon bits, grilled chicken and mushrooms.</p></div>
    <div class="entry"><div class="item"><span>Shrimp Fettuccini</span><span>$14.95</span></div><p class="desc">Pasta covered in creamy white wine sauce with grilled shrimp.</p></div>
    <div class="entry"><div class="item"><span>Montreal Steak Bowl</span><span>$16.95</span></div><p class="desc">Fettuccini topped with sautéed peppers, onions, mushrooms all mixed together with Montreal Steak Spices and topped with a flame grilled 6 oz. steak.</p></div>
    <div class="entry"><div class="item"><span>Lasagna</span><span>$11.95</span></div><p class="desc">Layers of pasta and meat sauce baked with lots of mozzarella cheese.</p></div>
    <div class="entry"><div class="item"><span>Traditional Spaghetti</span><span>$11.95</span></div><p class="desc">Spaghetti topped with our hearty homemade meat sauce.</p></div>
    <div class="entry"><div class="item"><span>Baked Spaghetti</span><span>$12.95</span></div><p class="desc">Spaghetti topped with meat sauce and cheese baked fresh from the oven.</p></div>
    <div class="entry"><div class="item"><span>Cajun Deluxe Penne</span><span>$14.95</span></div><p class="desc">Chicken, shrimp, onions, peppers, Italian sausages and tomato sauce finished in Cajun seasoning. This is a spicy one.</p></div>
    <div class="entry"><div class="item"><span>Meatballs</span><span>$1.60</span></div><p class="desc">Three tasty meatballs.</p></div>
    <div class="entry"><div class="item"><span>2 For 1</span><span>$18.95</span></div><p class="desc">Traditional Pasta, Lasagna, or Fettuccini and Alfredo Sauce</p></div>
    <div class="entry"><div class="item"><span>2 For 1</span><span>$20.95</span></div><p class="desc">Baked Pasta, Lasagna, or Fettuccini &amp; Alfredo Sauce</p></div>
  </div>

  <div class="photo" role="img" aria-label="Close-up photo of a pepperoni pizza" style="left:815px;top:500px;width:385px;height:276px;background:radial-gradient(circle at 30% 40%,#b8321f 0%,#e08a3a 18%,#f1c25a 30%,#c0401f 42%,#e9a04a 58%,#b8321f 72%,#d8772e 100%)"></div>
  <div class="abs web">www.hollingerpizza.example</div>
  <div class="abs info">
    <p>204-118 Larchwood Ave.,<br>Fort Ridgeway, AB</p>
    <p>Take out and Delivery only</p>
    <p>Delivery is Available:<br>Sun. - Wed.: 5pm - 10pm;<br>Thur. - Sat. : 5pm - 11pm</p>
  </div>
  <div class="photo" role="img" aria-label="Street map snapshot showing the restaurant location" style="left:1072px;top:636px;width:103px;height:104px;background:linear-gradient(135deg,#eef0e6,#dfe6d3);border:1px solid #999"></div>
  <p class="abs ownership-banner">NEW OWNERSHIP</p>

</main>
</body>
</html>
```